Design mobile friendly real estate and property management company landing page

Design a clean, crisp modern looking landing page that is mobile-friendly (must resize, preferably using bootstrap framework). Landing page will consist of heading with login area, company info, body consists of company description and services, a list of available rental properties with photos, and a footer with additional links and info. Working on updating with text for text areas marked A, B, and C on the layout pdf, but in meantime, lorem ipsum is fine. I can connect events to most buttons, etc. Just need the bootstrap and html functionality set up. Previous company website (which should not be relied upon) is www.qlbt.net This is somewhat of a template for a start, but looking for a more professional and modern design for the new website. But this gives an idea of the content and what needs to be displayed, and how.

Target Market(s)

Clients looking for a property management company that is efficient and well-organized.

Industry/Entity Type

Property Management

Coding

Coded - Design and coding required

Number of Pages Required

1 page

Font styles to use
Sans Serif

Colors
0355a3

Requirements
Must have
• Resize for the screen using bootstrap.
• Navigation that collapses for mobile devices
• Large text boxes and good solid spacing around all elements.
Nice to have
• for property images it would be nice if they can be swiped on touch enabled devices (to the next or previous image). And have navigation that can be clicked to next or previous images.
• Would be nice if a captcha verification was included on contact form.
Should not have
• Fancy or eccentric art

```html
<!DOCTYPE html>
<html lang="en">
<head>
<meta charset="utf-8">
<title>Harbor Crest Realty</title>
<link href="https://fonts.googleapis.com/css2?family=Cinzel:wght@600&family=Source+Sans+3:ital,wght@0,400;0,600;0,700;1,400&display=swap" rel="stylesheet">
<style>
:root{
  --navy:#0b1526;
  --nav:#3b3b3d;
  --blue:#0355a3;
  --ink:#1a1a1a;
  --grey-bg:#e8e8ea;
  --white:#ffffff;
  --muted:#b9bfc9;
  --icon-tone:#d9dde3;
}
*{box-sizing:border-box;margin:0;padding:0}
html,body{width:838px;height:1200px;overflow:hidden}
body{position:relative;font-family:"Source Sans 3",sans-serif;color:var(--ink);background:var(--white)}
.abs{position:absolute}

.site-header{left:0;top:0;width:838px;height:62px;background:var(--navy)}
.brand{color:var(--white);text-align:center;width:190px;white-space:nowrap}
.site-header .brand{left:70px;top:14px}
.brand .name{font-family:"Cinzel",serif;font-weight:600;font-size:17px;letter-spacing:1px;line-height:20px}
.brand .sub{font-family:"Cinzel",serif;font-weight:600;font-size:8.5px;letter-spacing:4px;line-height:14px}
.call{left:566px;top:20px;width:114px;height:24px;color:var(--white);white-space:nowrap}
.call .dot{position:absolute;left:0;top:0;width:24px;height:24px;border-radius:50%;background:var(--blue)}
.call .lbl{position:absolute;right:0;top:0;font-size:6px;font-weight:700}
.call .num{position:absolute;right:0;top:6px;font-size:13.5px;line-height:16px}
.login{left:697px;top:21px;width:52px;height:20px;border:1px solid var(--white);border-radius:2px;color:var(--white);font-family:"Cinzel",serif;font-weight:600;font-size:7px;display:flex;align-items:center;justify-content:center}

.main-nav{left:0;top:62px;width:838px;height:25px;background:var(--nav)}
.main-nav a{position:absolute;top:0;line-height:25px;font-size:7.5px;color:var(--white);text-decoration:none;text-transform:uppercase;white-space:nowrap}
.main-nav a.active::after{content:"";position:absolute;left:-9px;right:-9px;bottom:0;height:2px;background:var(--white)}

.hero{left:0;top:87px;width:838px;height:351px;background:linear-gradient(180deg,#4b6788 0%,#6b83a0 40%,#7b6a5a 62%,#3b5274 80%,#27436a 100%)}
.hero-copy{left:90px;top:145px;width:435px;color:var(--white)}
.hero-copy h1{font-size:17.5px;font-weight:700;margin-bottom:4px;line-height:22px}
.hero-copy p{font-size:7.6px;line-height:11.6px}
.badge{top:298px;height:30px;background:#f2f4f7;border-radius:2px}
.btn-ghost{left:90px;top:347px;width:73px;height:20px;border:1px solid var(--white);border-radius:2px;color:var(--white);font-family:"Cinzel",serif;font-weight:600;font-size:7px;display:flex;align-items:center;justify-content:center}

.contact{left:541px;top:113px;width:207px;height:299px;background:rgba(38,52,74,.92)}
.contact h2{position:absolute;left:0;top:15px;width:207px;text-align:center;color:var(--white);font-family:"Cinzel",serif;font-weight:600;font-size:15px}
.field{position:absolute;left:17px;width:173px;height:20px;background:var(--white);font-size:7.5px;font-style:italic;color:#8a8f96;padding:5px 6px}
.captcha{position:absolute;left:17px;top:210px;width:173px;height:43px;background:#f9f9f9;border:1px solid #d3d3d3;font-size:7.5px;color:#333}
.send{position:absolute;left:17px;top:256px;width:173px;height:26px;background:var(--blue);color:var(--white);font-size:7.5px;font-weight:700;display:flex;align-items:center;justify-content:center}

.rule{position:absolute;height:1px;background:var(--ink)}
.section-title{font-family:"Cinzel",serif;font-weight:600;font-size:14px;text-align:center;position:absolute}
.service-icon{position:absolute;width:66px;height:62px;background:var(--icon-tone);border-radius:4px}
.service-text{position:absolute;width:322px;font-size:7.6px;line-height:11.6px;text-align:center}
.btn-dark{position:absolute;width:73px;height:21px;background:var(--navy);border-radius:2px;color:var(--white);font-family:"Cinzel",serif;font-weight:600;font-size:7px;display:flex;align-items:center;justify-content:center}

.listings{left:0;top:750px;width:838px;height:296px;background:var(--grey-bg)}
.listings h2{position:absolute;left:90px;top:45px;font-family:"Cinzel",serif;font-weight:600;font-size:20px;color:var(--ink)}
.listing{position:absolute;left:90px;width:658px;height:80px;background:var(--white)}
.listing .photo{position:absolute;left:0;top:0;width:110px;height:80px}
.listing .arrows{position:absolute;left:87px;top:70px;width:22px;height:10px;background:rgba(40,40,40,.75)}
.listing .addr{position:absolute;left:110px;top:0;width:378px;height:17px;background:var(--blue);color:var(--white);font-size:7.5px;font-weight:600;line-height:17px;padding-left:18px;white-space:nowrap}
.listing .type{position:absolute;left:378px;top:0;width:280px;height:17px;background:var(--navy);clip-path:polygon(10px 0,100% 0,100% 100%,0 100%,10px 0);color:var(--white);font-size:7.5px;font-weight:600;line-height:17px;padding-left:22px;white-space:nowrap}
.specs{position:absolute;top:26px;font-size:7.2px;line-height:11.6px;white-space:nowrap}
.specs .k{display:inline-block;text-align:right;font-family:"Cinzel",serif;font-weight:600;font-size:6.6px;color:#333}
.specs .v{font-weight:700;padding-left:5px}
.desc{position:absolute;left:401px;top:26px;width:245px;font-size:7.4px;line-height:11.6px}

.site-footer{left:0;top:1046px;width:838px;height:154px;background:var(--navy);color:var(--white);text-align:center}
.site-footer .brand{left:324px;top:32px}
.foot-line{position:absolute;left:0;width:838px;font-size:7.2px;color:var(--white);white-space:nowrap}
.foot-line .k{color:#cfd3da}
.foot-copy{position:absolute;left:0;width:838px;top:114px;font-size:6.2px;color:var(--muted)}
</style>
</head>
<body>

<header class="site-header abs">
  <div class="brand abs"><div class="name">HARBOR CREST</div><div class="sub">REALTY</div></div>
  <div class="call abs">
    <span class="dot"><svg width="24" height="24" viewBox="0 0 24 24"><path d="M8.5 6.5l2 2-1.2 1.6c.8 1.7 2 2.9 3.6 3.7l1.6-1.2 2 2-1.4 1.9c-3.8-.5-7.6-4.3-8.1-8.1z" fill="#fff"/></svg></span>
    <span class="lbl">CALL US</span>
    <span class="num">(555) 214-0386</span>
  </div>
  <div class="login abs">LOGIN</div>
</header>

<nav class="main-nav abs">
  <a class="active" style="left:107px">Home</a>
  <a style="left:162px">For Rent</a>
  <a style="left:231px">For Sale</a>
  <a style="left:298px">Property Management</a>
  <a style="left:420px">Real Estate</a>
  <a style="left:498px">About</a>
</nav>

<section class="hero abs" role="img" aria-label="Coastal cliffs with a lighthouse above the ocean"></section>
<div class="hero-copy abs">
  <h1>Welcome to Harbor Crest Realty</h1>
  <p>Lorem ipsum dolor sit amet, consectetur adipiscing elit. Suspendisse porttitor fringilla fermentum. Sed ornare mi tortor, et pharetra tellus euismod sit amet. Pellentesque varius odio vel velit ultrices, vel mattis nisi ornare. Quisque ut elit in nibh pretium fermentum. Aliquam arcu nunc, porttitor non convallis ac, euismod et leo. Ut bibendum sagittis lacus quis tempus. Vivamus non lacus imperdiet, accumsan urna quis, rutrum velit. Phasellus varius ex tristique efficitur dictum. Cum sociis natoque penatibus et magnis dis parturient montes, nascetur ridiculus mus. Proin sit amet felis velit. Praesent vestibulum aliquam iaculis. Nulla posuere ante nibh, ut tempus eros efficitur vitae. Suspendisse potenti. Phasellus id mattis nisl. Maecenas ultricies nec lectus at blandit. Sed sed sem sed odio viverra congue ut vitae enim. Suspendisse ut eros ut nisl cursus ultricies. Etiam et sapien vitae est varius condimentum at eu orci. Proin in rhoncus sem, id interdum turpis. Etiam nec nulla auctor, mollis neque vel, vulputate lectus. In in dolor eget sem tristique tristique. Mauris lacinia leo ac nunc viverra, eget vehicula ex tincidunt. Vestibulum sem leo, gravida sit amet feugiat vitae, bibendum ac nulla pellentesque egestas nibh id quam bibendum.</p>
</div>
<div class="badge abs" style="left:90px;width:115px"></div>
<div class="badge abs" style="left:223px;width:50px"></div>
<div class="badge abs" style="left:290px;width:38px;border-radius:50%;background:none;border:2px solid #f2f4f7"></div>
<div class="btn-ghost abs">LEARN MORE</div>

<aside class="contact abs">
  <h2>CONTACT US</h2>
  <div class="rule" style="left:20px;top:35px;width:167px;background:#fff"></div>
  <div class="field" style="top:42px">Name</div>
  <div class="field" style="top:66px">Email</div>
  <div class="field" style="top:89px">Phone</div>
  <div class="field" style="top:113px">Subject/Property</div>
  <div class="field" style="top:137px;height:69px">Message</div>
  <div class="captcha">
    <span style="position:absolute;left:7px;top:13px;width:16px;height:16px;border:2px solid #c1c1c1;border-radius:2px;background:#fff"></span>
    <span style="position:absolute;left:30px;top:15px">I'm not a robot</span>
    <span style="position:absolute;right:10px;top:10px;width:18px;height:18px;background:#9aa7ba;border-radius:2px"></span>
  </div>
  <div class="send">SEND A MESSAGE</div>
</aside>

<h2 class="section-title" style="left:90px;top:486px;width:320px">PROPERTY MANAGEMENT</h2>
<div class="rule" style="left:160px;top:505px;width:180px"></div>
<div class="service-icon" role="img" aria-label="Icon of a hand holding a house" style="left:217px;top:534px"></div>
<p class="service-text" style="left:89px;top:612px">Cum sociis natoque penatibus et magnis dis parturient montes, nascetur ridiculus mus. Proin sit amet felis velit. Praesent vestibulum aliquam iaculis. Nulla posuere ante nibh, ut tempus eros efficitur vitae. Suspendisse potenti. Phasellus id mattis nisl. Maecenas ultricies nec lectus at blandit. Sed sed sem sed odio viverra congue ut vitae enim. Suspendisse ut eros ut nisl cursus ultricies. Etiam et sapien vitae est varius condimentum at eu orci. Proin in rhoncus</p>
<div class="btn-dark" style="left:213px;top:676px">LEARN MORE</div>

<h2 class="section-title" style="left:428px;top:486px;width:320px">REAL ESTATE</h2>
<div class="rule" style="left:502px;top:505px;width:172px"></div>
<div class="service-icon" role="img" aria-label="Icon of a property sign post" style="left:555px;top:534px"></div>
<p class="service-text" style="left:427px;top:612px">Praesent vestibulum aliquam iaculis. Nulla posuere ante nibh, ut tempus eros efficitur vitae. Suspendisse potenti. Phasellus id mattis nisl. Maecenas ultricies nec lectus at blandit. Sed sed sem sed odio viverra congue ut vitae enim. Suspendisse ut eros ut nisl cursus ultricies. Etiam et sapien vitae est varius condimentum at eu orci. Proin in rhoncus sem, id interdum turpis. Etiam nec nulla auctor, mollis neque vel, vulputate lectus. In in dolor eget sem tristique</p>
<div class="btn-dark" style="left:551px;top:676px">LEARN MORE</div>

<section class="listings abs">
  <h2>FEATURED LISTINGS</h2>

  <article class="listing" style="top:73px">
    <div class="photo" role="img" aria-label="Condo building with garages and a parked truck" style="background:linear-gradient(180deg,#8fa3b8 0%,#b59a77 45%,#8a8a84 75%,#c9c9c4 100%)"></div>
    <div class="arrows"></div>
    <div class="addr"><svg style="position:absolute;left:8px;top:4px" width="7" height="10" viewBox="0 0 7 10"><path d="M3.5 0C1.5 0 0 1.5 0 3.4 0 6 3.5 10 3.5 10S7 6 7 3.4C7 1.5 5.5 0 3.5 0zm0 5A1.6 1.6 0 1 1 3.5 1.8 1.6 1.6 0 0 1 3.5 5z" fill="#fff"/></svg>2716 Larkspur Ave, Bayview, CA 90004</div>
    <div class="type">2 Bedroom, 1 Bath Condo</div>
    <div class="specs" style="left:122px"><span class="k" style="width:40px">RENT:</span><span class="v">$1,600.00</span><br><span class="k" style="width:40px">AVAILABLE:</span><span class="v">6/1/2016</span><br><span class="k" style="width:40px">SQFT:</span><span class="v">675</span><br><span class="k" style="width:40px">LEASE:</span><span class="v">12 Months</span></div>
    <div class="specs" style="left:222px"><span class="k" style="width:60px">COMMUNITY:</span><span class="v">North Park</span><br><span class="k" style="width:60px">PARKING:</span><span class="v">2 assigned spaces off-s...</span><br><span class="k" style="width:60px">PETS:</span><span class="v">Inquire</span><br><span class="k" style="width:60px">LAUNDRY:</span><span class="v">On-Site</span></div>
    <p class="desc">Highly upgraded 2BR/1BA condo in gated North Park community. Unit features hardwood flooring, granite counters in kitchen and bathroom, appliances included. Two assigned off-street parking spaces. Must have excellent rental history, sorry, No ...</p>
  </article>

  <article class="listing" style="top:163px">
    <div class="photo" role="img" aria-label="Three-storey tan single-family home with garage" style="background:linear-gradient(180deg,#7fa0c8 0%,#c9a264 45%,#b38857 70%,#6f7d52 100%)"></div>
    <div class="arrows"></div>
    <div class="addr"><svg style="position:absolute;left:8px;top:4px" width="7" height="10" viewBox="0 0 7 10"><path d="M3.5 0C1.5 0 0 1.5 0 3.4 0 6 3.5 10 3.5 10S7 6 7 3.4C7 1.5 5.5 0 3.5 0zm0 5A1.6 1.6 0 1 1 3.5 1.8 1.6 1.6 0 0 1 3.5 5z" fill="#fff"/></svg>1938 Vista Marela, Bayview, CA 90006</div>
    <div class="type">3 Bedroom, 2.5 Bath Single-Family</div>
    <div class="specs" style="left:122px"><span class="k" style="width:40px">OFFERED</span><span class="v">$465,000.00</span><br><span class="k" style="width:40px">AT:</span><span class="v">PENDING</span><br><span class="k" style="width:40px">STATUS:</span><span class="v">2190</span><br><span class="k" style="width:40px">SQFT:</span><span class="v">$206.00</span></div>
    <div class="specs" style="left:222px"><span class="k" style="width:60px">COMMUNITY:</span><span class="v">Eastlake</span><br><span class="k" style="width:60px">PARKING:</span><span class="v">2 car attached garage</span><br><span class="k" style="width:60px">PETS:</span><span class="v"></span><br><span class="k" style="width:60px">LAUNDRY:</span><span class="v">Laundry Room</span></div>
    <p class="desc">Recently built tri-level detached home features 2190 sqft, 3 bedrooms plus large bonus room/family room, plus den/office, with 2 car attached garage in gated community. Unit features newer appliances, hardwood flooring downstairs, open kitchen, ...</p>
  </article>
</section>

<footer class="site-footer abs">
  <div class="brand abs"><div class="name">HARBOR CREST</div><div class="sub">REALTY</div></div>
  <div class="foot-line" style="top:82px"><span class="k">CA BRE LIC #:</span> 04419236 &nbsp;|&nbsp; <span class="k">PHONE:</span> (555) 214-0386 &nbsp;|&nbsp; <span class="k">FAX:</span> (555) 214-0392 &nbsp;|&nbsp; <span class="k">OFFICE:</span> 820 Pelican Way, Bayview, CA 90001 &nbsp;|&nbsp; <span class="k">EMAIL:</span> office@hcrealty.net</div>
  <div class="foot-line" style="top:97px"><span class="k">MAILING:</span> P.O. Box 31207 Bayview, CA 90002</div>
  <div class="foot-copy">©2016 Harbor Crest Realty. All Rights Reserved. &nbsp;Privacy Policy</div>
</footer>

</body>
</html>
```